Recruitment of Brindle Staffing for the UK market

I want a website for the UK market to attract businesses and companies to come to us for Philipine labour. We want an information site that gives all information on what we do and how we can recruit Philippine labour.
This is a recruitment site for companies to contact us with their requirements for skilled workers coming from the Philipines over to the UK to work.

Target Market(s)

Uk Companies and businesses who want Philipine skilled workers

Industry/Entity Type

REcruitment

Coding

Coded - Design and coding required

Number of Pages Required

5+ page

Font styles to use
Sans Serif

Colors
0054AA
0677BA
7BADD7
CADEEF
E8F1F8
0094D4
00A9DD
6FCCEA
C7EBF8
E9F6FB
EE7325
F08F49
F5BC92
FAE3D3
FDF4ED
EB3D1F
EC4F4E
F09395
F8D3D4
FCEDEE

Requirements
Must have
• Look professional and corperate with drop down menus for Home ,about, services,articles. training , contact us
Nice to have
• Look at Tovel recruitment- https://tovelrecruitment.example.co.uk/. This is my current site - https://www.brindlestaffing.example.com/
Should not have
• Cartoons or silly pictures , needs to be corperate looking

```html
<!DOCTYPE html>
<html lang="en">
<head>
<meta charset="utf-8">
<title>Brindle Staffing – Recruiting Skilled Philippine Workers</title>
<link rel="stylesheet" href="https://fonts.googleapis.com/css2?family=Poppins:wght@400;500;600;700&display=swap">
<style>
:root{
  --blue:#0054AA;
  --blue-mid:#0677BA;
  --blue-soft:#7BADD7;
  --blue-pale:#CADEEF;
  --blue-wash:#E8F1F8;
  --orange:#EE7325;
  --orange-mid:#F08F49;
  --orange-soft:#F5BC92;
  --orange-pale:#FAE3D3;
  --orange-wash:#FDF4ED;
  --red:#EB3D1F;
  --ink:#111318;
  --text:#2b2f36;
  --navy:#0b1833;
  --brand:#8a1d27;
}
*{box-sizing:border-box;margin:0;padding:0}
html,body{width:1200px;height:4464px;overflow:hidden;background:#fff}
body{position:relative;font-family:'Poppins',sans-serif;color:var(--text)}
.abs{position:absolute}
.btn{position:absolute;display:flex;align-items:center;justify-content:center;background:var(--orange);color:#fff;font-size:13px;font-weight:500;border-radius:2px}
.rule{position:absolute;height:3px;width:44px;background:var(--blue-pale)}
.section-title{position:absolute;font-weight:700;color:var(--ink);letter-spacing:1px;text-transform:uppercase}
.copy{position:absolute;font-size:13px;line-height:24.5px;color:var(--text)}

/* header */
.brand{position:absolute;left:173px;top:14px;font-size:26px;font-weight:700;color:var(--brand);letter-spacing:.3px}
.nav{position:absolute;top:20px;left:550px;display:flex;gap:36px;font-size:14px;color:#222}
.nav .active{color:var(--blue)}
.social-rail{position:absolute;left:80px;top:172px;width:14px;display:flex;flex-direction:column;align-items:center;gap:14px}
.social-rail span{width:10px;height:10px;border-radius:50%;background:var(--orange-soft)}
.social-rail span.on{width:28px;height:28px;background:var(--orange)}
.social-rail .scroll{font-size:10px;color:#777;writing-mode:vertical-rl;transform:rotate(180deg)}
.social-rail .line{width:1px;height:38px;background:#777}
.hero-title{position:absolute;left:171px;top:158px;font-size:33px;line-height:42px;font-weight:700;color:var(--ink);text-transform:uppercase}
.hero-title em{font-style:normal;color:var(--orange)}
.hero-photo{position:absolute;left:587px;top:69px;width:501px;height:397px;background:linear-gradient(115deg,var(--blue-pale) 0%,var(--blue-wash) 35%,var(--orange-mid) 60%,var(--orange) 100%);border-radius:4px}

/* inquiry */
.inquiry{position:absolute;left:168px;top:465px;width:875px;height:186px;background:var(--blue);border-radius:4px;box-shadow:0 14px 26px rgba(0,84,170,.25)}
.inquiry h2{position:absolute;top:20px;width:100%;text-align:center;color:#fff;font-size:25px;font-weight:500}
.inquiry .line{position:absolute;left:42px;right:42px;top:63px;height:1px;background:rgba(255,255,255,.2)}
.field{position:absolute;background:var(--blue-pale);font-size:12px;color:#333;padding:10px 18px;border-radius:2px}
.submit{position:absolute;left:746px;top:77px;width:86px;height:83px;background:var(--orange);color:#fff;font-weight:700;font-size:15px;line-height:19px;display:flex;align-items:center;justify-content:center;text-align:center;border-radius:2px}

/* contact strip */
.contact-strip{position:absolute;left:168px;top:907px;width:875px;height:70px;background:var(--orange-wash);border-radius:3px}
.contact-strip .label{position:absolute;left:0;top:0;width:222px;height:70px;background:var(--orange);color:#fff;font-size:22px;font-weight:500;display:flex;align-items:center;justify-content:center;border-radius:3px 0 0 3px}
.strip-item{position:absolute;font-size:13px;line-height:22px;color:#222}
.ico{position:absolute}

/* role cards */
.role{position:absolute;top:1034px;width:202px;height:299px;border-radius:4px;overflow:hidden}
.role span{position:absolute;bottom:16px;width:100%;text-align:center;color:#fff;font-size:14px;font-weight:500;letter-spacing:.5px}

/* map */
.map{position:absolute;left:337px;top:1563px;width:535px;height:311px;background:radial-gradient(ellipse at 55% 50%,var(--blue-soft) 0%,var(--blue-pale) 35%,rgba(232,241,248,.6) 60%,rgba(255,255,255,0) 75%)}

/* what we do */
.band-blue{position:absolute;left:9px;top:1955px;width:1186px;height:532px;background:var(--blue-wash)}
.photo-office{position:absolute;left:9px;top:2052px;width:556px;height:335px;background:linear-gradient(120deg,#cfd6df 0%,#e9edf2 45%,var(--blue-mid) 70%,#c8ced6 100%)}
.photo-meeting{position:absolute;left:677px;top:2630px;width:518px;height:297px;background:linear-gradient(120deg,#2a2f38 0%,#5a6270 40%,#dfe3e8 70%,#9aa3ad 100%)}

/* split */
.split-left{position:absolute;left:9px;top:3031px;width:595px;height:466px;background:linear-gradient(150deg,var(--blue-pale),#d9e7f4 55%,var(--blue-pale))}
.split-right{position:absolute;left:604px;top:3031px;width:591px;height:466px;background:linear-gradient(150deg,var(--orange-wash),#f8ebe0 55%,var(--orange-wash))}
.split-title{position:absolute;top:3137px;width:595px;text-align:center;font-size:32px;font-weight:700;color:var(--ink);letter-spacing:1.5px}
.split-copy{position:absolute;top:3213px;text-align:center;font-size:13px;line-height:29.6px;color:#222}

/* services */
.svc{position:absolute;top:3653px;width:269px;height:297px;background:var(--orange-wash);border-radius:8px;text-align:center}
.svc.featured{top:3653px;background:var(--orange)}
.svc .circle{position:absolute;left:80px;top:-55px;width:110px;height:110px;border-radius:50%;background:var(--orange);border:6px solid var(--orange-pale);display:flex;align-items:center;justify-content:center}
.svc.featured .circle{background:var(--orange-mid);border-color:var(--orange-soft);top:-63px}
.svc h3{position:absolute;top:80px;width:100%;font-size:15px;font-weight:600;color:var(--ink)}
.svc .bar{position:absolute;top:113px;left:122px;width:26px;height:2px;background:var(--orange)}
.svc p{position:absolute;top:132px;left:20px;right:20px;font-size:12.5px;line-height:21.5px;color:#333}
.svc .more{position:absolute;top:219px;left:77px;width:115px;height:35px;background:var(--orange);color:#fff;font-size:13px;display:flex;align-items:center;justify-content:center;border-radius:2px}
.svc.featured h3,.svc.featured p{color:#fff}
.svc.featured .bar{background:#fff}
.svc.featured .more{background:#fff;color:var(--ink)}

/* footer */
.footer{position:absolute;left:9px;top:4055px;width:1186px;height:409px;background:var(--navy)}
.footer .brand-f{position:absolute;left:162px;top:110px;font-size:24px;font-weight:700;color:#fff}
.footer .dots{position:absolute;left:162px;top:164px;display:flex;gap:11px}
.footer .dots span{width:27px;height:27px;border-radius:50%;background:#2b66d3}
.footer h4{position:absolute;top:108px;font-size:15px;font-weight:600;color:#fff;letter-spacing:1px}
.footer .link{position:absolute;font-size:13px;color:#dfe4ee}
.footer .frow{position:absolute;font-size:13px;line-height:20px;color:#dfe4ee}
.footer .copyright{position:absolute;top:338px;width:100%;text-align:center;font-size:13px;color:#dfe4ee}
</style>
</head>
<body>

<header>
  <div class="brand">Brindle Staffing</div>
  <nav class="nav">
    <span class="active">Home</span><span>About</span><span>Services</span><span>Articles</span><span>Training</span><span>Contact Us</span>
  </nav>
</header>

<aside class="social-rail" aria-label="Social links">
  <span></span><span class="on"></span><span></span><span></span>
  <div class="scroll">scroll</div><div class="line"></div>
</aside>

<section class="hero">
  <h1 class="hero-title">Recruiting and<br>placing skilled<br><em>Philippine workers</em><br>into UK companies</h1>
  <a class="btn" style="left:168px;top:347px;width:165px;height:37px">Contact Us Today</a>
  <div class="hero-photo" role="img" aria-label="Two smiling Filipino workers in orange safety vests and hard hats holding plans"></div>
</section>

<form class="inquiry">
  <h2>Quick Inquiry</h2>
  <div class="line"></div>
  <div class="field" style="left:44px;top:77px;width:223px;height:37px">First name*</div>
  <div class="field" style="left:279px;top:77px;width:221px;height:37px">Last name*</div>
  <div class="field" style="left:44px;top:126px;width:223px;height:34px">Phone*</div>
  <div class="field" style="left:279px;top:126px;width:221px;height:34px">Email*</div>
  <div class="field" style="left:512px;top:77px;width:223px;height:83px">Message</div>
  <div class="submit">SUBMIT<br>NOW</div>
</form>

<section class="about">
  <h2 class="section-title" style="left:0;width:1200px;text-align:center;top:745px;font-size:33px">What the business is about</h2>
  <div class="rule" style="left:584px;top:805px"></div>
  <p class="copy" style="left:240px;width:720px;top:819px;text-align:center">We source skilled workers directly from the Philippines to work in the UK. With offices , training locations and specialist recruiters we can find the highest quality individuals to add value and resources to any UK buisness. We delivery quality based on vast experience over a number of years.</p>

  <div class="contact-strip">
    <div class="label">Contact Details</div>
    <svg class="ico" style="left:244px;top:17px" width="14" height="20" viewBox="0 0 14 20"><path d="M7 0C3 0 0 3 0 7c0 5 7 13 7 13s7-8 7-13c0-4-3-7-7-7z" fill="#EE7325"/><circle cx="7" cy="7" r="2.6" fill="#fff"/></svg>
    <div class="strip-item" style="left:274px;top:12px">Orchard Mews, Kingsfield Kingsfield<br>KF4 2 United Kingdom</div>
    <svg class="ico" style="left:584px;top:11px" width="18" height="18" viewBox="0 0 24 24"><path d="M6.6 10.8a15 15 0 006.6 6.6l2.2-2.2c.3-.3.7-.4 1-.2 1.1.4 2.3.6 3.6.6.6 0 1 .4 1 1V20c0 .6-.4 1-1 1A17 17 0 013 4c0-.6.4-1 1-1h3.5c.6 0 1 .4 1 1 0 1.3.2 2.5.6 3.6.1.3 0 .7-.2 1z" fill="#EE7325"/></svg>
    <div class="strip-item" style="left:616px;top:10px">07700900123</div>
    <svg class="ico" style="left:584px;top:42px" width="19" height="14" viewBox="0 0 19 14"><rect x="0" y="0" width="19" height="14" rx="1" fill="#EE7325"/><path d="M1 1l8.5 7L18 1" stroke="#fff" stroke-width="1.5" fill="none"/></svg>
    <div class="strip-item" style="left:616px;top:37px">sales@brindlestaffing.example.com</div>
  </div>

  <div class="role" style="left:168px;background:linear-gradient(180deg,#e9eef3,#6f8fc6 60%,#3f5f9e)" role="img" aria-label="Nurse in blue scrubs holding a tablet"><span>NURSE</span></div>
  <div class="role" style="left:392px;background:linear-gradient(180deg,#d9dde2,#6fa2c6 55%,#3b6d94)" role="img" aria-label="Group of smiling staff nurses in teal uniforms"><span>STAFF NURSE</span></div>
  <div class="role" style="left:617px;background:linear-gradient(180deg,#e8e4dc,#d9b44a 30%,#b6a6b0 60%,#6c6670)" role="img" aria-label="Engineers wearing a yellow hard hat"><span>ENGINEER</span></div>
  <div class="role" style="left:841px;background:linear-gradient(180deg,#7a8a84,#b9bfc4 40%,#8c8f8f 70%,#5b5044)" role="img" aria-label="Welder in white hard hat working on a pipe"><span>WELDER</span></div>
</section>

<section class="together">
  <h2 class="section-title" style="left:0;width:1200px;text-align:center;top:1428px;font-size:33px">Working together</h2>
  <div class="rule" style="left:584px;top:1487px"></div>
  <p class="copy" style="left:0;width:1200px;top:1502px;text-align:center">We recruit the finest talent available with our dedicated 200 strong team.<br>Our centres are highlighted in <span style="color:var(--red)">Red Dots</span> on the map.</p>
  <div class="map" role="img" aria-label="Map of the Philippines with recruitment centres marked in Baguio, Manila, Batangas, Bacolod and Davao"></div>
</section>

<section class="what-we-do">
  <div class="band-blue"></div>
  <div class="photo-office" role="img" aria-label="Two businessmen reviewing work at a desk with a computer and a UK flag"></div>
  <h2 class="section-title" style="left:653px;top:2066px;font-size:32px">What we do</h2>
  <div class="rule" style="left:653px;top:2121px"></div>
  <p class="copy" style="left:653px;width:390px;top:2136px">Our company has been estabilished in the Philippines for over 20 years. We have mainly been recruiting philippine workers for the off shore industry in asia but since brexit and the new rules on skilled workers entering the UK we have been working with UK companies who now have chance to recruit some of the finest hard working talent from the Philippines for their companies..</p>
  <a class="btn" style="left:653px;top:2330px;width:165px;height:36px">Contact Us Today</a>
</section>

<section class="how-we-help">
  <h2 class="section-title" style="left:171px;top:2634px;font-size:32px">How we help</h2>
  <div class="rule" style="left:171px;top:2691px"></div>
  <p class="copy" style="left:171px;width:380px;top:2706px">We work with companies to find skilled workers that meet the UK requirements for Visas and work permits. We guide you through the whole process and deliver highly trained people that add value to your business. We are here to help both the companies and the Philippino people to gain a better standard of living for their families.</p>
  <div class="photo-meeting" role="img" aria-label="Business people in suits shaking hands across a meeting table"></div>
</section>

<section class="split">
  <div class="split-left" role="presentation"></div>
  <div class="split-right" role="presentation"></div>
  <h2 class="split-title" style="left:9px">WHERE TO START</h2>
  <p class="split-copy" style="left:55px;width:505px">We need to know what your issues are and how we can understand the personnal you require, over what time frame and the number of employees you need. Once this is estabilished we start sourcing workers in the Philippines that meet your criteria while starting the process in the UK to be able to have all the documents in place to deliver your company hard working skilled individuals.</p>
  <h2 class="split-title" style="left:604px;width:591px">CONTACT US TODAY</h2>
  <p class="split-copy" style="left:670px;width:470px">Please contact us today with your requirements, this can be care workers, chef, welders, pipe fitters, caravan cabinet makers, medical workers. The UK list of required skills is extensive and the Philippines offersenglish speaking highly qualified hard working employees. Contact us today and make that first step to a highly motivated , quality skilled workforce.</p>
</section>

<section class="services">
  <div class="svc" style="left:168px">
    <div class="circle"><svg width="46" height="46" viewBox="0 0 46 46" fill="none" stroke="#fff" stroke-width="2"><rect x="10" y="6" width="26" height="34" rx="2"/><path d="M16 15h14M16 21h14M16 27h10M16 33h8"/></svg></div>
    <h3>UK SKILLED WORKERS LIST</h3><div class="bar"></div>
    <p>The UK government since brexit have developed a new system based on points...</p>
    <div class="more">Read More</div>
  </div>
  <div class="svc featured" style="left:471px">
    <div class="circle"><svg width="46" height="46" viewBox="0 0 46 46" fill="none" stroke="#fff" stroke-width="2"><rect x="10" y="6" width="26" height="34" rx="2"/><circle cx="18" cy="17" r="4"/><path d="M25 15h7M25 20h7M15 28h17M15 34h12"/></svg></div>
    <h3>SPONSOR LICENCE</h3><div class="bar"></div>
    <p>If you have areas of your business that meet the entry requirements of skilled labour...</p>
    <div class="more">Read More</div>
  </div>
  <div class="svc" style="left:774px">
    <div class="circle"><svg width="46" height="46" viewBox="0 0 46 46" fill="none" stroke="#fff" stroke-width="2"><rect x="8" y="14" width="22" height="24" rx="2"/><circle cx="32" cy="30" r="8"/><path d="M32 26v4l3 2M13 21h12M13 27h8"/></svg></div>
    <h3>RECRUITMENT TIMELINE</h3><div class="bar"></div>
    <p>Brief us on the job profiles-this is passed on to our teams in the Philippines.</p>
    <div class="more">Read More</div>
  </div>
</section>

<footer class="footer">
  <div class="brand-f">Brindle Staffing</div>
  <div class="dots" aria-label="Social links"><span></span><span></span><span></span><span></span></div>

  <h4 style="left:438px">QUICK LINKS</h4>
  <div class="link" style="left:438px;top:139px">› Home</div>
  <div class="link" style="left:438px;top:176px">› About</div>
  <div class="link" style="left:438px;top:213px">› Services</div>
  <div class="link" style="left:573px;top:139px">› Articles</div>
  <div class="link" style="left:573px;top:176px">› Training</div>
  <div class="link" style="left:573px;top:213px">› Contact Us</div>

  <h4 style="left:746px">CONTACT DETAILS</h4>
  <svg class="ico" style="left:746px;top:141px" width="12" height="17" viewBox="0 0 14 20"><path d="M7 0C3 0 0 3 0 7c0 5 7 13 7 13s7-8 7-13c0-4-3-7-7-7z" fill="#fff"/><circle cx="7" cy="7" r="2.6" fill="#0b1833"/></svg>
  <div class="frow" style="left:774px;top:138px">Orchard Mews, Kingsfield Kingsfield<br>KF4 2 United Kingdom</div>
  <div style="position:absolute;left:774px;top:181px;width:268px;height:1px;background:rgba(255,255,255,.15)"></div>
  <svg class="ico" style="left:745px;top:189px" width="15" height="15" viewBox="0 0 24 24"><path d="M6.6 10.8a15 15 0 006.6 6.6l2.2-2.2c.3-.3.7-.4 1-.2 1.1.4 2.3.6 3.6.6.6 0 1 .4 1 1V20c0 .6-.4 1-1 1A17 17 0 013 4c0-.6.4-1 1-1h3.5c.6 0 1 .4 1 1 0 1.3.2 2.5.6 3.6.1.3 0 .7-.2 1z" fill="#fff"/></svg>
  <div class="frow" style="left:774px;top:186px">07700900123</div>
  <div style="position:absolute;left:774px;top:210px;width:268px;height:1px;background:rgba(255,255,255,.15)"></div>
  <svg class="ico" style="left:745px;top:219px" width="16" height="12" viewBox="0 0 19 14"><rect width="19" height="14" rx="1" fill="#fff"/><path d="M1 1l8.5 7L18 1" stroke="#0b1833" stroke-width="1.5" fill="none"/></svg>
  <div class="frow" style="left:774px;top:214px">sales@brindlestaffing.example.com</div>

  <div style="position:absolute;left:0;right:0;top:318px;height:1px;background:rgba(255,255,255,.08)"></div>
  <div class="copyright">© 2023 Brindle Staffing Ltd. All Rights Reserved</div>
</footer>

</body>
</html>
```